Flyer-Design für Uhren und Schmuck
Zielgruppe
Unser Online Shop ist Zirbelglanz.ch und unser Ladenlokal Walzinger Uhren & Schmuck GmbH.
Wir sind eine Uhren & Schmuck Bijouterie, welche im laufe des nächsten Jahres schließt.
Daher brauchen wir ansprechende Flyers für unseren Ausverkauf im Ladenlokal.
Aufgabenstellung
Wenig Text & mehr Bilder benutzen. ( Siehe Online Shop www.zirbelglanz.ch )
20%, 30%, 50% werden unsere Rabatte sein. Bitte erwähnen Sie das Wort TOTAL - AUSVERKAUF.
Marken welche vorkommen sollen: Aurel Wendt, Veloria, Lukas Brevin, Ravok, Tanru, Sternwinder, Plint, Ombre du Val, Gioie di Brenta.

```html
<!DOCTYPE html>
<html lang="de">
<head>
<meta charset="utf-8">
<title>Walzinger – Total Ausverkauf</title>
<link rel="stylesheet" href="https://fonts.googleapis.com/css2?family=Arvo:wght@400;700&family=Montserrat:wght@800&family=Playfair+Display:wght@600&family=Caveat:wght@400&family=Roboto:wght@300&display=swap">
<style>
  :root {
    --ink: #15131a;
    --white: #ffffff;
    --gold-light: #ecc66c;
    --gold-mid: #d9a94a;
    --gold-deep: #b7812c;
    --brown-text: #2a1a0c;
    --photo-dark: #2b170c;
    --photo-mid: #7a4a25;
    --photo-warm: #b57a45;
    --photo-skin: #d8a776;
    --logo-tone: #e8d6cb;
    --mark-tone: rgba(236, 214, 205, 0.75);
  }
  html, body {
    margin: 0;
    padding: 0;
    overflow: hidden;
    background: #ffffff;
  }
  .flyer {
    position: relative;
    width: 846px;
    height: 1200px;
    overflow: hidden;
    background: var(--photo-dark);
  }
  .photo {
    position: absolute;
    inset: 0;
    background:
      radial-gradient(ellipse 45% 35% at 82% 18%, var(--photo-skin), transparent 70%),
      radial-gradient(ellipse 55% 30% at 35% 92%, var(--photo-warm), transparent 70%),
      radial-gradient(ellipse 60% 40% at 20% 55%, var(--photo-mid), transparent 75%),
      linear-gradient(160deg, #3a2213 0%, var(--photo-mid) 45%, #3b2112 80%, var(--photo-dark) 100%);
  }
  .brand {
    position: absolute;
    left: 50px;
    top: 84px;
    margin: 0;
    font-family: "Arvo", serif;
    font-weight: 400;
    font-size: 46px;
    letter-spacing: 4px;
    color: var(--logo-tone);
  }
  .gold-panel {
    position: absolute;
    left: 242px;
    top: 470px;
    width: 420px;
    height: 400px;
    background: linear-gradient(180deg, var(--gold-light) 0%, var(--gold-mid) 60%, var(--gold-deep) 100%);
    opacity: 0.95;
  }
  .decor {
    position: absolute;
    inset: 0;
  }
  .ribbon {
    position: absolute;
    left: 118px;
    top: 318px;
    width: 490px;
    height: 58px;
    background: var(--ink);
    transform: rotate(-5deg);
    color: var(--white);
    font-family: "Playfair Display", serif;
    font-weight: 600;
    font-size: 30px;
    line-height: 58px;
    text-align: center;
    letter-spacing: 1px;
  }
  .headline {
    position: absolute;
    left: 170px;
    top: 374px;
    width: 430px;
    height: 96px;
    background: var(--ink);
    transform: rotate(-4deg);
    margin: 0;
    color: var(--white);
    font-family: "Montserrat", sans-serif;
    font-weight: 800;
    font-size: 66px;
    line-height: 96px;
    text-align: center;
  }
  .discount {
    position: absolute;
    left: 372px;
    top: 458px;
    width: 232px;
    height: 100px;
    background: var(--ink);
    transform: rotate(-4deg);
    color: var(--white);
    text-align: center;
  }
  .discount-label {
    display: block;
    font-family: "Montserrat", sans-serif;
    font-weight: 800;
    font-size: 20px;
    margin-top: 6px;
  }
  .discount-value {
    display: block;
    font-family: "Arvo", serif;
    font-weight: 400;
    font-size: 58px;
    line-height: 62px;
  }
  .store-info {
    position: absolute;
    left: 242px;
    top: 672px;
    width: 420px;
    text-align: center;
    color: var(--brown-text);
    font-family: "Arvo", serif;
    font-weight: 700;
  }
  .store-info p { margin: 0; }
  .address { font-size: 34px; line-height: 40px; }
  .hours { font-size: 30px; line-height: 46px; }
  .address + .hours { margin-top: 10px; }
  .valid-until {
    position: absolute;
    left: 30px;
    top: 1160px;
    transform: rotate(-90deg);
    transform-origin: left top;
    font-family: "Roboto", sans-serif;
    font-weight: 300;
    font-size: 17px;
    color: var(--logo-tone);
    white-space: nowrap;
  }
  .brand-marks {
    position: absolute;
    left: 100px;
    top: 1025px;
    width: 680px;
    display: grid;
    grid-template-columns: repeat(3, 222px);
    row-gap: 20px;
    font-family: "Caveat", cursive;
    font-size: 34px;
    color: var(--mark-tone);
  }
</style>
</head>
<body>
<div class="flyer">
  <div class="photo" role="img" aria-label="Sepia-Foto einer Frau mit Armbändern aus Perlen und Schmuckkugeln an den Handgelenken"></div>

  <p class="brand">walzinger</p>

  <div class="gold-panel"></div>

  <svg class="decor" width="846" height="1200" viewBox="0 0 846 1200" aria-hidden="true">
    <g fill="none" stroke="#15131a" stroke-width="5" stroke-linecap="round">
      <line x1="140" y1="290" x2="250" y2="270"/>
      <line x1="160" y1="440" x2="210" y2="436"/>
      <line x1="150" y1="462" x2="200" y2="458"/>
      <line x1="250" y1="555" x2="350" y2="515"/>
      <line x1="262" y1="578" x2="362" y2="545"/>
      <line x1="600" y1="548" x2="515" y2="612"/>
      <line x1="600" y1="548" x2="580" y2="632"/>
      <line x1="505" y1="600" x2="700" y2="600"/>
      <line x1="600" y1="310" x2="660" y2="306"/>
      <circle cx="262" cy="472" r="9"/>
      <circle cx="688" cy="538" r="9"/>
    </g>
  </svg>

  <div class="ribbon">TOTAL AUSVERKAUF</div>
  <h1 class="headline">MEGA SALE</h1>
  <div class="discount">
    <span class="discount-label">discount up to</span>
    <span class="discount-value">50 %</span>
  </div>

  <div class="store-info">
    <p class="address">Lindenweg 14</p>
    <p class="address">8820 Wädenswil</p>
    <p class="hours">Mo-Fr 09 - 18 Uhr</p>
    <p class="hours">Sa 10 - 15 Uhr</p>
  </div>

  <div class="valid-until">Nur bis 30.11.2022</div>

  <div class="brand-marks">
    <span>Markenlogo</span><span>Markenlogo</span><span>Markenlogo</span>
    <span>Markenlogo</span><span>Markenlogo</span><span>Markenlogo</span>
  </div>
</div>
</body>
</html>
```